Webdesign
Zielgruppe
Briefing für die neue Website von TELORI GmbH
Allgemeine Informationen:
Name des Unternehmens: TELORI GmbH
Branche: Maschinenbau
Zweck der Website: Eine Unternehmenswebsite, die informiert, was die Firma macht und es potenziellen Kunden oder Partnern ermöglicht, in Kontakt zu treten.
Zielgruppe:
Hauptzielgruppe: Anlagenbauer, Maschinenbauer, Anlagenbetreiber aus verschiedenen Branchen.
Design-Anforderungen: Die Zielgruppe erwartet Professionalität und Klarheit, also sollte die Website eine hohe Qualität, Professionalität und Benutzerfreundlichkeit reflektieren.
Design-Vorlieben:
Farbschema & Stil: Das Design sollte sich an den bereitgestellten Logos orientieren. Der gewünschte Stil ist modern und klar.
Inspirationsquellen: Die Logos des Unternehmens, die dem Briefing beigefügt werden.
Inhalt und Struktur:
Einseitiges Design: Die Website sollte nur eine Seite zum Herunterscrollen haben.
Unternehmensvorstellung: Ein kurzer Abschnitt, der beschreibt, wer TELORI GmbH ist und was das Unternehmen macht.
Leistungsübersicht: Eine klare Darstellung der Dienstleistungen oder Produkte, die TELORI GmbH anbietet. Dies kann durch Symbole, kurze Texte oder Bilder dargestellt werden.
Kontaktmöglichkeit: Ein Kontaktformular oder zumindest klare Kontaktinformationen (Telefon, E-Mail, Adresse), so dass Besucher leicht in Kontakt treten können.
Aufgabenstellung
siehe oben

```html
<!DOCTYPE html>
<html lang="de">
<head>
<meta charset="utf-8">
<title>TELORI GmbH – Maschinenbau</title>
<link href="https://fonts.googleapis.com/css2?family=Montserrat:wght@400;500;600;700&display=swap" rel="stylesheet">
<style>
:root{
  --red:#b50f10;
  --red-bright:#d0151a;
  --dark:#2a2a2a;
  --ink:#222;
  --grey-bg:#f1f1f1;
  --line:#d8d8d8;
  --yellow:#fdc737;
  --white:#fff;
}
*{box-sizing:border-box;margin:0;padding:0}
html,body{width:1200px;height:3458px;overflow:hidden}
body{position:relative;background:var(--white);font-family:"Montserrat",Arial,sans-serif;color:var(--ink)}
.abs{position:absolute}

/* hero */
.hero{left:0;top:0;width:1200px;height:544px;clip-path:polygon(0 0,100% 0,100% 507px,0 544px)}
.hero-photo{position:absolute;inset:0;background:radial-gradient(ellipse at 62% 35%,#5a4a3a 0%,#2c2622 45%,#141212 100%)}
.logo{left:152px;top:30px;display:flex;align-items:center;gap:10px;color:var(--white);font-weight:700;font-size:34px;letter-spacing:1px}
.logo .dot{width:18px;height:18px;background:var(--red-bright);border-radius:50%}
.nav{left:659px;top:0;display:flex}
.nav a{display:block;height:54px;line-height:54px;padding:0 18px;color:var(--white);font-size:13px;font-weight:600;text-decoration:none}
.nav a.active{background:var(--red-bright)}
.hero h1{left:146px;top:178px;width:460px;color:var(--white);font-size:37px;font-weight:600;line-height:43px}
.hero-sub{left:148px;top:274px;color:var(--white);font-size:16px}
.btn-phone{left:150px;top:329px;width:228px;height:48px;background:var(--red-bright);color:var(--white);font-size:20px;font-weight:600;display:flex;align-items:center;justify-content:center;gap:14px}
.dots{display:flex;gap:7px}
.dots span{width:8px;height:8px;border-radius:50%;background:var(--red-bright)}
.dots span.on{background:var(--white)}
.hero-dots{left:567px;top:474px}

/* about */
h2{color:var(--red);font-weight:600;font-size:27px}
.about-title{left:148px;top:682px}
.about-text{left:148px;top:730px;width:490px;font-size:12.5px;line-height:18.7px}
.about-visual{left:729px;top:577px;width:326px;height:356px}

/* services */
.band{left:0;width:1200px;background:var(--grey-bg)}
.band-services{top:980px;height:955px;clip-path:polygon(0 43px,100% 0,100% 912px,0 955px)}
.center-title{left:0;width:1200px;text-align:center}
.card{width:420px;height:340px;background:var(--white);border:1px solid var(--line)}
.card-head{height:42px;background:var(--red);color:var(--white);font-weight:600;font-size:15px;text-align:center;line-height:42px}
.card-img{height:164px}
.card-text{padding:16px 40px 0 20px;font-size:11.4px;line-height:15.5px;color:#333}
.card-btn{display:block;margin:22px 0 0 147px;width:104px;height:30px;background:var(--red);color:var(--white);font-size:12.5px;font-weight:600;text-align:center;line-height:30px}

/* strengths */
.strength{width:283px;height:191px;background:var(--white);border:1px solid var(--line);padding:22px 16px 0 94px}
.strength svg{position:absolute;left:24px;top:22px}
.strength h3{color:var(--red);font-weight:500;font-size:15.5px;line-height:19px;text-transform:uppercase;margin-bottom:8px}
.strength p{font-size:11.8px;line-height:16.2px;color:#333}

/* testimonials */
.band-quotes{top:2507px;height:392px;clip-path:polygon(0 46px,100% 0,100% 100%,0 100%)}
.quote-text{width:410px;font-size:12.5px;line-height:18.7px;color:#333}
.quote-name{color:var(--red);font-size:12.5px;font-weight:600}
.qmark{color:#cfcfcf;font-size:96px;font-weight:700;line-height:1;font-family:Georgia,serif}
.t-dots span{background:#cfcfcf;width:7px;height:7px}
.t-dots span.on{background:var(--red-bright)}

/* contact */
.contact{left:0;top:2899px;width:1200px;height:476px;background:linear-gradient(160deg,#d52027 0%,#c41b21 50%,#b8171c 100%)}
.contact-sub{color:var(--white);font-size:12.5px}
.field{background:var(--white);height:38px;font-size:12.5px;color:#555;padding:0 13px;line-height:38px}
.field.area{height:106px;line-height:normal;padding-top:16px}
.send{left:518px;top:3184px;width:168px;height:37px;background:var(--yellow);color:#222;font-weight:600;font-size:15px;text-align:center;line-height:37px}
.info{color:var(--white);font-size:17px}
.info.small{font-size:12.5px;line-height:18.7px}

/* footer */
.footer{left:0;top:3375px;width:1200px;height:83px;background:var(--dark)}
.footer-logo{left:152px;top:3402px;color:#6a6a6a;font-weight:700;font-size:24px;display:flex;align-items:center;gap:8px}
.footer-logo .dot{width:12px;height:12px;border-radius:50%;background:#6a6a6a}
.socials{left:537px;top:3411px;display:flex;gap:19px}
.socials span{width:10px;height:10px;border-radius:50%;background:#666}
.copy{right:150px;top:3409px;color:#888;font-size:12px}
</style>
</head>
<body>

<!-- Hero -->
<section class="abs hero">
  <div class="hero-photo" role="img" aria-label="Ingenieur mit Schutzhelm in einer Industriehalle, Blick von hinten"></div>
  <div class="abs logo"><span class="dot"></span>TELORI</div>
  <nav class="abs nav">
    <a class="active" href="#">Startseite</a>
    <a href="#">Wer wir sind</a>
    <a href="#">Was wir tun</a>
    <a href="#">Kontakt</a>
  </nav>
  <h1 class="abs">Lorem ipsum dolor sit amet, consectetur</h1>
  <p class="abs hero-sub">Lorem ipsum dolor sit amet, consectetur</p>
  <div class="abs btn-phone">
    <svg width="20" height="20" viewBox="0 0 24 24" fill="none" stroke="#fff" stroke-width="2"><path d="M5 3h4l2 5-2.5 1.5a11 11 0 0 0 6 6L16 13l5 2v4a2 2 0 0 1-2 2A16 16 0 0 1 3 5a2 2 0 0 1 2-2z"/></svg>
    0800.555.210
  </div>
  <div class="abs dots hero-dots"><span class="on"></span><span></span><span></span><span></span><span></span></div>
</section>

<!-- About -->
<h2 class="abs about-title">Wer wir sind</h2>
<p class="abs about-text">TELORI ist ein führendes Unternehmen im Bereich moderner Maschinenbau. Wir sind spezialisiert auf die Konzeption, Konstruktion und Herstellung maßgeschneiderter Maschinen und Anlagen, die den höchsten Ansprüchen der heutigen Industrie gerecht werden.</p>
<svg class="abs about-visual" viewBox="0 0 326 356">
  <defs><radialGradient id="team"><stop offset="0" stop-color="#4d7fb5"/><stop offset="1" stop-color="#1b2e4a"/></radialGradient></defs>
  <circle cx="163" cy="178" r="150" fill="none" stroke="#3a3a3a" stroke-width="26" stroke-dasharray="470 1000" transform="rotate(180 163 178)"/>
  <circle cx="163" cy="178" r="150" fill="none" stroke="#c8161b" stroke-width="26" stroke-dasharray="470 1000"/>
  <circle cx="163" cy="178" r="122" fill="#ffffff"/>
  <circle cx="163" cy="178" r="112" fill="url(#team)" role="img" aria-label="Team von Ingenieuren bei der Arbeit an einem Bildschirm"/>
</svg>

<!-- Services -->
<div class="abs band band-services"></div>
<h2 class="abs center-title" style="top:1043px">Was wir tun</h2>

<article class="abs card" style="left:149px;top:1111px">
  <div class="card-head">Quis ipsum suspendisse</div>
  <div class="card-img" role="img" aria-label="CNC-Maschine mit blauen Pneumatikleitungen" style="background:linear-gradient(135deg,#5b6b78,#2d3a45 60%,#8a8f92)"></div>
  <p class="card-text">Lorem ipsum dolor sit amet, consectetur adipiscing elit, sed do eiusmod tempor incididunt ut labore et dolore magna aliqua. Quis ipsum suspendisse ultrices gravida.</p>
  <span class="card-btn">Kontakt</span>
</article>
<article class="abs card" style="left:629px;top:1111px">
  <div class="card-head">Quis ipsum suspendisse</div>
  <div class="card-img" role="img" aria-label="Fertigungshalle mit Industrierobotern" style="background:linear-gradient(135deg,#b8bec4,#7d848b 50%,#c4763a)"></div>
  <p class="card-text">Lorem ipsum dolor sit amet, consectetur adipiscing elit, sed do eiusmod tempor incididunt ut labore et dolore magna aliqua. Quis ipsum suspendisse ultrices gravida.</p>
  <span class="card-btn">Kontakt</span>
</article>
<article class="abs card" style="left:149px;top:1490px">
  <div class="card-head">Quis ipsum suspendisse</div>
  <div class="card-img" role="img" aria-label="Gelbe Roboterarme mit digitalem Netzwerk" style="background:linear-gradient(135deg,#1e3550,#3d5a78 50%,#b89a3a)"></div>
  <p class="card-text">Lorem ipsum dolor sit amet, consectetur adipiscing elit, sed do eiusmod tempor incididunt ut labore et dolore magna aliqua. Quis ipsum suspendisse ultrices gravida.</p>
  <span class="card-btn">Kontakt</span>
</article>
<article class="abs card" style="left:629px;top:1490px">
  <div class="card-head">Quis ipsum suspendisse</div>
  <div class="card-img" role="img" aria-label="Automatisierte Produktionslinie" style="background:linear-gradient(135deg,#9aa2a8,#5e666d 55%,#c9cdd0)"></div>
  <p class="card-text">Lorem ipsum dolor sit amet, consectetur adipiscing elit, sed do eiusmod tempor incididunt ut labore et dolore magna aliqua. Quis ipsum suspendisse ultrices gravida.</p>
  <span class="card-btn">Kontakt</span>
</article>

<!-- Strengths -->
<h2 class="abs center-title" style="top:1990px">Unsere Stärken</h2>

<div class="abs strength" style="left:149px;top:2048px">
  <svg width="48" height="60" viewBox="0 0 48 60" fill="none" stroke="#c8161b" stroke-width="2"><path d="M24 8a16 16 0 0 0-9 29v6h18v-6A16 16 0 0 0 24 8z"/><path d="M16 48h16M18 53h12"/><circle cx="24" cy="24" r="6"/><path d="M24 1v4M4 24h4M40 24h4M9 9l3 3M39 9l-3 3"/></svg>
  <h3>Innovation</h3>
  <p>Wir setzen modernste CAD/CAM-Software und CNC-Technologien ein, um Präzision und Effizienz in der Produktion sicherzustellen.</p>
</div>
<div class="abs strength" style="left:459px;top:2048px">
  <svg width="48" height="60" viewBox="0 0 48 60" fill="none" stroke="#c8161b" stroke-width="2"><circle cx="24" cy="22" r="18"/><circle cx="24" cy="22" r="11"/><path d="M24 15l2 5h5l-4 3 2 5-5-3-5 3 2-5-4-3h5z"/><path d="M14 37l-4 16 7-4 4 6 3-14M34 37l4 16-7-4-4 6"/></svg>
  <h3>Qualität</h3>
  <p>Unsere hochqualifizierten Ingenieure und Techniker arbeiten mit Leidenschaft daran, innovative Lösungen zu entwickeln und höchste Qualitätsstandards zu erfüllen.</p>
</div>
<div class="abs strength" style="left:766px;top:2048px">
  <svg width="56" height="56" viewBox="0 0 56 56" fill="none" stroke="#c8161b" stroke-width="2"><path d="M46 16A22 22 0 0 0 8 24M10 40a22 22 0 0 0 38-8"/><path d="M46 6v10H36M10 50V40h10"/><path d="M30 12L20 30h9l-3 14 11-19h-9z"/></svg>
  <h3>Nachhaltigkeit</h3>
  <p>Umweltfreundlichkeit und Nachhaltigkeit sind integraler Bestandteil unserer Philosophie. Wir integrieren diese Prinzipien in all unsere Produkte und Produktionsprozesse.</p>
</div>
<div class="abs strength" style="left:302px;top:2268px">
  <svg width="58" height="56" viewBox="0 0 58 56" fill="none" stroke="#c8161b" stroke-width="2"><path d="M29 4l3 7h7l-6 4 2 7-6-4-6 4 2-7-6-4h7zM12 12l2 4h4l-3 3 1 4-4-2-4 2 1-4-3-3h4zM46 12l2 4h4l-3 3 1 4-4-2-4 2 1-4-3-3h4z"/><path d="M2 36h8v16H2zM10 38h14c4 0 6 4 2 6h-8M26 44l20-8c4-1 6 3 2 5L26 52H10"/></svg>
  <h3>Kundenzufrie-<br>denheit</h3>
  <p>Bei TELORI steht die Zufriedenheit unserer Kunden an erster Stelle. Wir arbeiten eng mit Ihnen zusammen, um Ihre individuellen Anforderungen zu verstehen und zu erfüllen.</p>
</div>
<div class="abs strength" style="left:609px;top:2268px;padding-top:34px">
  <svg width="58" height="50" viewBox="0 0 58 50" fill="none" stroke="#c8161b" stroke-width="2" style="top:30px"><circle cx="34" cy="28" r="18"/><path d="M34 16v12l7 5M30 4h8M34 4v6M2 20h10M6 28h8M2 36h10"/></svg>
  <h3>Schnelligkeit</h3>
  <p>Unsere kurzen Lieferzeiten und erstklassiger Kundensupport gewährleisten, dass Sie stets bestens betreut werden.</p>
</div>

<!-- Testimonials -->
<div class="abs band band-quotes"></div>
<div class="abs qmark" style="left:146px;top:2570px">“</div>
<h2 class="abs center-title" style="top:2592px">Was unser Kunde sagt</h2>
<p class="abs quote-text" style="left:148px;top:2656px">Quis ipsum suspendisse ultrices gravida. Risus commodo viverra maecenas accumsan lacus vel facilisis. Risus commodo viverra maecenas accumsan lacus vel facilisis.  Lorem ipsum dolor sit amet, consectetur adipiscing elit, sed do eiusmod tempor incididunt ut labore et dolore magna aliqua.</p>
<p class="abs quote-name" style="left:148px;top:2768px">- Lukas Brenner</p>
<p class="abs quote-text" style="left:634px;top:2656px">Lorem ipsum dolor sit amet, consectetur adipiscing elit, sed do eiusmod tempor incididunt ut labore et dolore magna aliqua. Quis ipsum suspendisse ultrices gravida. Risus commodo viverra maecenas accumsan lacus vel facilisis.</p>
<p class="abs quote-name" style="left:636px;top:2768px">- Marta Velden</p>
<div class="abs qmark" style="left:1004px;top:2774px">”</div>
<div class="abs dots t-dots" style="left:567px;top:2845px"><span class="on"></span><span></span><span></span><span></span><span></span></div>

<!-- Contact -->
<section class="abs contact" role="img" aria-label="Rot eingefärbte Fabrikhalle im Hintergrund"></section>
<h2 class="abs center-title" style="top:2933px;color:#fff">Schneller Kontakt</h2>
<p class="abs center-title contact-sub" style="top:2972px">Risus commodo viverra maecenas accumsan lacus vel facilisis.</p>
<div class="abs field" style="left:331px;top:3011px;width:174px">Name</div>
<div class="abs field" style="left:519px;top:3011px;width:167px">Email</div>
<div class="abs field" style="left:698px;top:3011px;width:170px">Telefon</div>
<div class="abs field area" style="left:331px;top:3061px;width:537px">Wie können wir Ihnen helfen?</div>
<div class="abs send">SENDEN</div>

<svg class="abs" style="left:234px;top:3278px" width="20" height="24" viewBox="0 0 20 24" fill="#fff"><path d="M10 0a9 9 0 0 0-9 9c0 7 9 15 9 15s9-8 9-15a9 9 0 0 0-9-9zm0 13a4 4 0 1 1 0-8 4 4 0 0 1 0 8z"/></svg>
<p class="abs info small" style="left:274px;top:3264px;width:200px;word-break:break-all">XXXXXXXXXXXXXXXXXXXXXXXX XXXXXXXXXXXXXXXXXXXXXXXX XXXXXXXXXXXXXXXXXXX</p>
<svg class="abs" style="left:541px;top:3276px" width="24" height="17" viewBox="0 0 24 17" fill="none" stroke="#fff" stroke-width="1.6"><rect x="1" y="1" width="22" height="15"/><path d="M1 1l11 9 11-9"/></svg>
<p class="abs info" style="left:581px;top:3273px">kontakt@telori.de</p>
<svg class="abs" style="left:797px;top:3275px" width="20" height="20" viewBox="0 0 24 24" fill="none" stroke="#fff" stroke-width="2"><path d="M5 3h4l2 5-2.5 1.5a11 11 0 0 0 6 6L16 13l5 2v4a2 2 0 0 1-2 2A16 16 0 0 1 3 5a2 2 0 0 1 2-2z"/></svg>
<p class="abs info" style="left:836px;top:3272px;font-size:19px">0800.555.210</p>

<!-- Footer -->
<footer class="abs footer"></footer>
<div class="abs footer-logo"><span class="dot"></span>TELORI</div>
<div class="abs socials"><span></span><span></span><span></span><span></span><span></span></div>
<p class="abs copy">© 2023 telori.de</p>

</body>
</html>
```